Consumer Finance flyer

This flyer is being developed to help our outside sales people.

Please develop a master template flyer with key bullet points similar to uploaded file.

The main graphic will be replaced as we build out a flyer for each market segment. Example: Healthcare, Dental, Remodeling etc.
so we will keep the bullet point but replace the graphic for each custom vertical industry.

Need flyer to have an editable section at the bottom so the sales person can add their name and phone number and print the flyer.

please incorporate the LendaVista logo attached. So it will be branded lendavista.

Industry/Entity Type

Dental

```html
<!DOCTYPE html>
<html lang="en">
<head>
<meta charset="utf-8">
<title>LendaVista Flyer</title>
<link href="https://fonts.googleapis.com/css2?family=Josefin+Sans:wght@300&family=Lilita+One&family=Open+Sans:wght@400;700&family=Ubuntu:wght@500&display=swap" rel="stylesheet">
<style>
  :root {
    --green: #6aa632;
    --green-dark: #4e8a1e;
    --green-light: #a9d46a;
    --orange: #e8764c;
    --blue: #2a86c8;
    --ink: #2b2b2b;
    --grey-logo: #555a5e;
    --page: #ffffff;
    --backdrop: #dedede;
  }
  * { margin: 0; padding: 0; box-sizing: border-box; }
  html, body { width: 1200px; height: 1000px; overflow: hidden; background: var(--backdrop); }
  body { font-family: "Open Sans", Arial, sans-serif; color: var(--ink); }

  .flyer {
    position: absolute; left: 280px; top: 30px;
    width: 640px; height: 940px;
    background: var(--page);
    overflow: hidden;
    box-shadow: 0 4px 18px rgba(0,0,0,.18);
  }
  .wave { position: absolute; left: 0; width: 640px; display: block; }
  .wave-top { top: 0; height: 110px; }
  .wave-bottom { bottom: 0; height: 170px; }

  .brand {
    position: absolute; left: 42px; top: 92px;
    display: flex; align-items: center; gap: 14px;
  }
  .brand-name {
    font-family: "Josefin Sans", Arial, sans-serif; font-weight: 300;
    font-size: 60px; letter-spacing: 6px; color: var(--grey-logo);
    text-transform: uppercase; line-height: 1;
  }
  .brand-dot { width: 26px; height: 26px; border-radius: 50%; background: var(--green); }

  .hero-photo {
    position: absolute; left: 330px; top: 170px; width: 310px; height: 400px;
    background: linear-gradient(180deg, #b9c7d3 0%, #8e9eab 35%, #c9d2da 65%, #ffffff 100%);
  }

  .headline { position: absolute; left: 42px; top: 176px; width: 290px; font-family: "Ubuntu", Arial, sans-serif; font-weight: 500; color: var(--orange); line-height: 1; }
  .headline .line-a { display: block; font-size: 34px; }
  .headline .line-b { display: block; font-size: 58px; margin-top: 6px; }
  .headline .line-c { display: block; font-size: 32px; text-align: right; margin-top: 8px; }

  .intro { position: absolute; left: 42px; top: 340px; width: 318px; font-size: 10.5px; line-height: 1.4; font-weight: 700; }
  .intro .lead { text-transform: uppercase; margin-bottom: 12px; }

  .tagline {
    position: absolute; left: 42px; top: 448px; width: 320px;
    font-family: "Lilita One", Arial, sans-serif; color: var(--green);
    font-size: 33px; line-height: 1.1;
  }

  .benefits { position: absolute; left: 42px; top: 540px; width: 150px; font-size: 9.6px; line-height: 1.22; text-transform: uppercase; padding-left: 14px; }
  .benefits li { margin-bottom: 1px; }

  .lenders { position: absolute; left: 212px; top: 532px; width: 140px; font-size: 9.6px; line-height: 1.3; }
  .lenders p { margin-bottom: 10px; }
  .lenders h4 { font-size: 9.6px; font-weight: 700; }

  .market-watch { position: absolute; left: 352px; top: 578px; width: 260px; font-size: 9.6px; line-height: 1.3; }
  .market-chart {
    float: left; width: 88px; height: 48px; margin: 6px 8px 4px 0;
    background: linear-gradient(135deg, #f3e6b0, #d9c27a 60%, #b8a25a);
  }
  .market-watch h3 { font-size: 13px; color: var(--blue); font-weight: 700; text-transform: uppercase; }

  .contact { position: absolute; left: 390px; top: 728px; font-size: 10px; line-height: 1.5; }
  .contact h3 { font-size: 11.5px; font-weight: 700; text-transform: uppercase; margin-bottom: 2px; }
  .contact li { list-style: none; display: flex; align-items: center; gap: 8px; }
  .contact svg { width: 10px; height: 10px; fill: #555; }

  .address {
    position: absolute; left: 42px; top: 858px; width: 220px;
    color: #fff; font-size: 10.5px; line-height: 1.3;
  }
</style>
</head>
<body>
  <main class="flyer">
    <svg class="wave wave-top" viewBox="0 0 640 110" preserveAspectRatio="none">
      <path d="M0 0H640V40C520 30 420 70 300 62C180 54 90 20 0 45Z" fill="var(--green)"/>
      <path d="M0 45C90 20 180 54 300 62C420 70 520 30 640 40V60C520 55 420 88 300 80C180 72 90 40 0 62Z" fill="var(--green-light)"/>
      <path d="M0 62C90 40 180 72 300 80C420 88 520 55 640 60" fill="none" stroke="var(--green)" stroke-width="2"/>
    </svg>

    <div class="brand">
      <span class="brand-name">LendaVista</span>
      <span class="brand-dot"></span>
    </div>

    <div class="hero-photo" role="img" aria-label="Photo of three business people reviewing documents in a bright office"></div>

    <h1 class="headline">
      <span class="line-a">A New</span>
      <span class="line-b">Financing</span>
      <span class="line-c">Focus</span>
    </h1>

    <div class="intro">
      <p class="lead">Fundara is addressing the needs of business and their consumers by planting the seeds for a growing and financially secure future.</p>
      <p>You now have multiple financing and payment options to help more clients today. You can now confidently tell the world that you have fast and easy solutions for their needs.</p>
    </div>

    <h2 class="tagline">Helping you achieve customer satisfaction</h2>

    <ul class="benefits">
      <li>Several interest free plans</li>
      <li>0% for 6 to 18 months</li>
      <li>Revolving lines of credit</li>
      <li>Term loans from 2 to 20yrs*</li>
      <li>National lenders compete</li>
      <li>Easy single page app</li>
      <li>Lenient requirements</li>
      <li>No default interest rates</li>
      <li>No prepayment penalties</li>
      <li>May request overnight</li>
      <li>Rates from 6.95%*</li>
      <li>Plus no credit app option</li>
      <li>Approvals in minutes</li>
      <li>May combine offers</li>
      <li>Credit approvals 24 to 48 hrs</li>
    </ul>

    <div class="lenders">
      <p>Multiple lenders will process your clients with only ONE credit application. We will contact your clients for security and to help expedite the lending process for optimum performance and satisfaction. Co-borrowers are welcome to help income profile of your clients. This can overcome reservations.</p>
      <h4>We provide:</h4>
      <p>Custom application website<br>Online payment calculators.<br>Back office status access.<br>Live assistance.<br>*multiple programs available*</p>
    </div>

    <section class="market-watch">
      <div class="market-chart" role="img" aria-label="Photo of a pen resting on a printed market chart"></div>
      <h3>Market Watch</h3>
      <p>Fundara is a Open Credit Group Company. We are committed to continue to broaden your scope of opportunity and expand your market and potential. We are always looking to add lending exclusives from more National Lenders to increase sales and grow your business even more!</p>
    </section>

    <section class="contact">
      <h3>Dana Mercer</h3>
      <ul>
        <li><svg viewBox="0 0 10 10"><rect x="2.5" y="0" width="5" height="10" rx="1"/></svg>866-555-0142</li>
        <li><svg viewBox="0 0 10 10"><path d="M0 2h10v6H0z M0 2l5 3.5L10 2" /></svg>dana@fundara.net</li>
        <li><svg viewBox="0 0 10 10"><path d="M0 1h10v6H0z M4 7h2v1.5h2V10H2V8.5h2z"/></svg>www.fundaraline.com</li>
        <li><svg viewBox="0 0 10 10"><path d="M1 9l1-3 5-5 2 2-5 5z"/></svg>480-555-0176 direct</li>
      </ul>
    </section>

    <svg class="wave wave-bottom" viewBox="0 0 640 170" preserveAspectRatio="none">
      <path d="M0 30C150 -5 300 70 430 55C530 44 600 10 640 0V25C590 45 520 80 420 88C290 98 150 45 0 60Z" fill="var(--green-light)"/>
      <path d="M0 60C150 45 290 98 420 88C520 80 590 45 640 25V170H0Z" fill="var(--green)"/>
      <path d="M0 75C160 62 300 112 430 100C530 92 600 60 640 45" fill="none" stroke="#fff" stroke-width="2" opacity=".8"/>
      <path d="M0 120C180 105 330 150 640 110V170H0Z" fill="var(--green-dark)" opacity=".45"/>
    </svg>

    <p class="address">Fundara, a Open Credit Group, LLC company. 1450 W. Harlow Ave, Cheyenne, WY 82001<br>Arizona Offices: 4820 West Mesa Rd. 12-204 Chandler, AZ 85226</p>
  </main>
</body>
</html>
```